Flooring & Interior Design showroom

Just bought this business- Kestrel Lane Flooring & Interiors. Love our logo (we are on Kestrel Lane )and colors
Forest green, gold and black
Love that the back lists everything we do. We no longer have plenotilex but need to add in LVP/ SPC and need to take out vantor shadehub logo at the bottom and use the quib logo instead (maybe? open to suggestions)

Not in love with our cards- I want a higher end look
I hate the gradient poop color we have now.
Would love if they were all black - maybe or ??
or had a foil or embossing?

```html
<!DOCTYPE html>
<html lang="en">
<head>
<meta charset="utf-8">
<title>Kestrel Lane Flooring &amp; Interiors – Business Card</title>
<link href="https://fonts.googleapis.com/css2?family=Montserrat:wght@400;500;600;700&display=swap" rel="stylesheet">
<style>
  :root {
    --backdrop: #a9a9a9;
    --card: #111111;
    --forest: #2f6b45;
    --forest-dark: #244f35;
    --gold: #c9a55a;
    --gold-soft: #b8975a;
    --text: #e9e4d8;
    --muted: #bdb6a6;
  }
  * { box-sizing: border-box; margin: 0; padding: 0; }
  html, body {
    width: 900px; height: 1200px; overflow: hidden;
    background: var(--backdrop);
    font-family: "Montserrat", Arial, sans-serif;
    color: var(--text);
  }
  .card {
    position: absolute; left: 80px; width: 742px; height: 441px;
    background: var(--card); border-radius: 40px; overflow: hidden;
    box-shadow: 0 6px 14px rgba(0,0,0,0.35);
  }
  .card--front { top: 131px; }
  .card--back { top: 638px; }

  .wordmark { position: absolute; color: var(--gold); font-weight: 600; line-height: 1.05; }
  .wordmark__name, .wordmark__trade { display: block; }
  .card--front .wordmark { left: 42px; top: 72px; }
  .card--front .wordmark__name { font-size: 38px; }
  .card--front .wordmark__trade { font-size: 17px; margin-top: 10px; letter-spacing: 1px; }
  .card--back .wordmark { left: 0; right: 0; top: 80px; text-align: center; }
  .card--back .wordmark__name { font-size: 62px; }
  .card--back .wordmark__trade { font-size: 27px; margin-top: 16px; letter-spacing: 2px; }

  .person { position: absolute; right: 38px; top: 44px; text-align: right; }
  .person__name { color: var(--gold); font-size: 26px; font-weight: 600; line-height: 1.1; }
  .person__role { color: var(--muted); font-size: 16px; margin-top: 4px; }
  .edge-tab { position: absolute; right: 0; top: 52px; width: 16px; height: 37px; background: var(--forest); }

  .contacts { position: absolute; right: 38px; top: 118px; list-style: none; }
  .contacts li {
    display: flex; justify-content: flex-end; align-items: center;
    height: 25.5px; font-size: 16px; color: var(--text);
  }
  .contacts svg { width: 15px; height: 15px; margin-left: 14px; fill: var(--gold); }

  .divider { position: absolute; left: 38px; right: 38px; top: 277px; border: 0; border-top: 1.5px solid var(--gold-soft); }

  .address { position: absolute; left: 38px; top: 316px; display: flex; font-size: 16px; color: var(--text); line-height: 21px; }
  .address svg { width: 14px; height: 18px; fill: var(--gold); margin: 4px 14px 0 0; }

  .partners { position: absolute; right: 38px; top: 336px; display: flex; align-items: center; gap: 14px; }
  .partners__name { font-size: 22px; font-weight: 700; color: var(--text); }
  .partners__dot { width: 24px; height: 24px; border-radius: 50%; background: var(--gold); }

  .sweep { position: absolute; left: 0; top: 0; width: 742px; height: 441px; }
  .license { position: absolute; right: 50px; bottom: 10px; color: var(--text); font-size: 15px; }

  .services { position: absolute; list-style: none; font-size: 16px; color: var(--text); }
  .services li { position: relative; height: 19.6px; line-height: 19.6px; padding-left: 19px; }
  .services li::before {
    content: ""; position: absolute; left: 0; top: 7px;
    width: 6px; height: 6px; border-radius: 50%; background: var(--gold);
  }
  .services--floors { left: 50px; top: 280px; }
  .services--windows { left: 309px; top: 297px; }
  .services--textiles { left: 542px; top: 297px; }
</style>
</head>
<body>

<section class="card card--front" aria-label="Card front">
  <div class="wordmark">
    <span class="wordmark__name">Kestrel Lane</span>
    <span class="wordmark__trade">FLOORING &amp; INTERIORS</span>
  </div>

  <div class="person">
    <p class="person__name">Mara Ellison</p>
    <p class="person__role">Owner/ Designer</p>
  </div>
  <span class="edge-tab"></span>

  <ul class="contacts">
    <li>(555) 210-4837
      <svg viewBox="0 0 16 16"><path d="M1 6c0-2 2-3 7-3s7 1 7 3v1h-4V5.5H5V7H1zM3 8h10l1 6H2z"/></svg></li>
    <li>555-648-2290
      <svg viewBox="0 0 16 16"><path d="M4 0h8v16H4zM5.5 2v10h5V2z"/></svg></li>
    <li>555.319. 7064
      <svg viewBox="0 0 16 16"><path d="M5 2h6v4h3v9H2V6h3zM6.5 3.5v2.5h3V3.5zM4 9v4h8V9z"/></svg></li>
    <li>hello@kestrellaneflooring.com
      <svg viewBox="0 0 16 16"><path d="M1 3h14v1l-7 5-7-5zM1 6l7 5 7-5v7H1z"/></svg></li>
    <li>www.kestrellaneflooring.com
      <svg viewBox="0 0 16 16"><circle cx="8" cy="8" r="7"/><path d="M4 5c2 0 2 2 4 2s1 3-1 4-1 3-1 3" stroke="#111" stroke-width="1.3" fill="none"/></svg></li>
  </ul>

  <hr class="divider">

  <div class="address">
    <svg viewBox="0 0 14 18"><path d="M7 0a7 7 0 0 1 7 7c0 5-7 11-7 11S0 12 0 7a7 7 0 0 1 7-7zm0 4a3 3 0 1 0 0 6 3 3 0 0 0 0-6z"/></svg>
    <p>128 Kestrel Lane<br>Harbor Point, CA 90000</p>
  </div>

  <div class="partners">
    <span class="partners__name">quib</span>
    <span class="partners__name">Alderwick</span>
    <span class="partners__dot"></span>
  </div>

  <svg class="sweep" viewBox="0 0 742 441" aria-hidden="true">
    <path d="M135 441 Q300 401 560 399 L742 399 L742 441 Z" fill="var(--forest)"/>
    <path d="M40 441 Q260 396 560 392" fill="none" stroke="var(--gold)" stroke-width="2"/>
  </svg>
  <p class="license">CA Lic # 482917</p>
</section>

<section class="card card--back" aria-label="Card back">
  <div class="wordmark">
    <span class="wordmark__name">Kestrel Lane</span>
    <span class="wordmark__trade">FLOORING &amp; INTERIORS</span>
  </div>

  <ul class="services services--floors">
    <li>LVP/ SPC</li><li>Area rugs</li><li>Hardwood</li><li>Cork</li>
    <li>Bamboo</li><li>Laminate</li><li>Vinyl</li>
  </ul>
  <ul class="services services--windows">
    <li>Shades</li><li>Sheers</li><li>Shutters</li><li>Drapes</li>
    <li>Bedding</li><li>Upholstery</li>
  </ul>
  <ul class="services services--textiles">
    <li>Blinds</li><li>Carpet</li><li>verticals</li><li>Bed spreads</li>
    <li>Fabric</li><li>valances</li>
  </ul>
</section>

</body>
</html>
```